Social Movement/Church Plant Website - KindHearth.com

We need a website for our church plant startup, however we want the focus of the landing page to be around #kindhearth - that we are an organization that is FOR our town (Loveland). The site will include serving project events, social events, a place to sign up for emails, a blog, a place to give, etc. All the elements we know we want are currently at kindhearth.com . Please check this for copy.

We want this to be easy to edit as a non-developer.

I have included several logos with our colors, as well as an ai file to give you an idea of how we want the design to look and feel - also includes our branded fonts

Target Market(s)

People who live in the Northern CO area

Font styles to use
Serif
Sans Serif

Requirements
Must have
• Events (serve and social), Blog section, A place to get involved - where to give and to sign up for emails. Must match our branding colors and style hex 4c7991.
Should not have
• Should not be focused on the actual church plant on the home page. There can be some back end stuff about it, but the focus should be #kindhearth.

```html
<!DOCTYPE html>
<html lang="en">
<head>
<meta charset="utf-8">
<title>KindHearth – For Our Town</title>
<link href="https://fonts.googleapis.com/css2?family=Playfair+Display:wght@500;600;700&family=Open+Sans:wght@400;600;700&display=swap" rel="stylesheet">
<style>
:root{
  --brand:#4c7991;
  --brand-dark:#3d6479;
  --brand-deep:#2e4e60;
  --brand-soft:#7ea3b6;
  --ink:#222;
  --text:#555;
  --muted:#888;
  --line:#e6e6e6;
  --panel:#f2f2f2;
  --footer:#1b1b1b;
  --white:#fff;
  --serif:"Playfair Display",Georgia,serif;
  --sans:"Open Sans",Arial,sans-serif;
}
*{box-sizing:border-box;margin:0;padding:0}
html,body{width:1200px;height:4433px;overflow:hidden}
body{font-family:var(--sans);color:var(--text);background:var(--white);position:relative}
.abs{position:absolute}
h1,h2,h3,h4{font-family:var(--serif);font-weight:600}
a{color:inherit;text-decoration:none}

/* header */
.site-header{position:absolute;left:0;top:0;width:1200px;height:112px;background:var(--white)}
.brand{position:absolute;left:88px;top:30px;font-family:var(--serif);font-weight:600;font-size:36px;color:var(--brand)}
.nav{position:absolute;top:46px;left:640px;font-family:var(--sans);font-size:15px;color:var(--ink)}
.nav a{position:absolute;white-space:nowrap}
.nav .active{color:var(--brand);font-weight:600}
.nav .social-sq{width:15px;height:15px;background:var(--ink);border-radius:3px;top:2px}

/* hero */
.hero{position:absolute;left:0;top:112px;width:1200px;height:680px}
.hero-photo{position:absolute;inset:0;background:linear-gradient(180deg,#a9b4b2 0%,#7f8f83 45%,#5e7560 75%,#4c6450 100%)}
.hero-title{position:absolute;left:0;width:1200px;top:228px;text-align:center;font-family:var(--serif);font-weight:600;font-style:italic;font-size:124px;color:var(--white)}
.btn{display:inline-block;font-family:var(--sans);font-weight:600;color:var(--white);background:var(--brand);border-radius:30px;text-align:center}
.hero .btn{position:absolute;left:508px;top:432px;width:184px;height:54px;line-height:54px;font-size:16px;box-shadow:0 4px 0 var(--brand-deep)}
.hero-wave{position:absolute;left:0;top:560px}

/* action cards */
.action{position:absolute;top:822px;width:296px;height:232px;background:var(--white);box-shadow:0 0 0 1px var(--line),0 6px 16px rgba(0,0,0,.08);text-align:center}
.action.featured{background:var(--brand);color:var(--white)}
.action svg{margin-top:20px}
.action h3{font-size:22px;font-weight:500;color:var(--brand);margin-top:8px}
.action.featured h3{color:var(--white)}
.action p{font-size:13.5px;line-height:21px;padding:0 36px;margin-top:10px}
.action .tag{position:absolute;left:86px;bottom:-14px;width:124px;height:30px;line-height:30px;font-size:12px;font-weight:600;color:var(--white);background:var(--brand);clip-path:polygon(10% 0,100% 0,90% 100%,0 100%)}
.action.featured .tag{background:var(--white);color:var(--ink)}

/* event bands */
.band{position:absolute;left:0;width:1200px;background:linear-gradient(135deg,#4c7991 0%,#5a88a0 40%,#44708a 100%)}
.band-title{position:absolute;left:0;width:1200px;text-align:center;font-size:34px;color:var(--white)}
.event{position:absolute;width:252px;height:340px;background:var(--white);box-shadow:0 4px 12px rgba(0,0,0,.12)}
.event-photo{height:165px;background:linear-gradient(135deg,#9aa6a8,#6b8170 60%,#a8998a)}
.event h4{font-family:var(--sans);font-size:12.5px;font-weight:600;color:var(--brand);line-height:19px;padding:16px 34px 0 34px}
.event p{font-size:12.5px;line-height:19px;padding:8px 34px 0 34px;color:var(--text)}
.event .more{display:block;padding:6px 34px 0;font-size:12.5px;color:var(--brand);font-weight:600;text-decoration:underline}
.date{position:absolute;width:63px;height:68px;background:var(--white);text-align:center;font-family:var(--sans);font-weight:700;color:var(--ink)}
.date b{display:block;font-size:17px;padding-top:8px}
.date span{display:block;font-size:12px;font-weight:600;margin-top:8px;border-top:1px solid var(--line);padding-top:6px}

/* story */
.story-title{position:absolute;left:92px;top:1818px;font-size:38px;color:var(--brand)}
.story-sub{position:absolute;left:92px;top:1874px;font-size:27px;font-weight:500;color:var(--brand);font-family:var(--serif)}
.story-text{position:absolute;left:92px;top:1926px;width:520px;font-size:15.5px;line-height:29px;color:var(--ink)}
.story .btn{position:absolute;top:2082px;height:44px;line-height:44px;font-size:15px}
.story-frame{position:absolute;left:644px;top:1808px;width:466px;height:352px}

/* testimonials */
.section-title{position:absolute;left:0;width:1200px;text-align:center;font-size:34px;color:var(--brand)}
.avatar{position:absolute;border-radius:50%;background:radial-gradient(circle at 50% 40%,#e7d8cd,#c9b3a4);box-shadow:0 3px 10px rgba(0,0,0,.15);border:4px solid var(--white)}
.author{position:absolute;left:0;width:1200px;text-align:center;font-size:14px;font-weight:600;color:var(--brand);top:3260px}
.author-loc{position:absolute;left:0;width:1200px;text-align:center;font-size:13px;color:var(--ink);top:3290px}
.quote{position:absolute;left:210px;width:780px;top:3326px;text-align:center;font-size:14.5px;line-height:27px;color:var(--muted)}

/* blog */
.post{position:absolute;left:100px;width:470px;background:var(--panel)}
.post .date{left:0;top:0;background:var(--brand);color:var(--white);width:58px;height:64px}
.post .date span{border-color:rgba(255,255,255,.4)}
.post h4{position:absolute;left:76px;top:12px;width:384px;white-space:nowrap;font-family:var(--sans);font-size:13px;font-weight:700;color:var(--ink)}
.post .meta{position:absolute;left:76px;top:38px;width:370px;font-size:11px;color:var(--muted)}
.post .meta i{position:absolute;right:0;font-style:normal}
.post .excerpt{position:absolute;left:0;top:64px;width:470px;height:86px;background:var(--white);border:1px solid var(--line);padding:18px 20px;font-size:12.5px;line-height:20px;color:var(--text)}
.feature{position:absolute;left:600px;top:3570px;width:500px;height:312px;background:linear-gradient(160deg,#8d9a9c,#5c7468 55%,#435a50)}
.feature .date{left:0;top:0;background:var(--brand);color:var(--white);width:58px;height:64px}
.feature .date span{border-color:rgba(255,255,255,.4)}
.feature .tools{position:absolute;right:0;top:0;width:92px;height:56px;background:var(--brand)}
.feature p{position:absolute;left:20px;bottom:22px;width:440px;font-size:13px;line-height:22px;color:var(--white)}

/* footer */
.footer{position:absolute;left:0;top:3950px;width:1200px;height:483px}
.footer-base{position:absolute;left:0;top:80px;width:1200px;height:403px;background:var(--footer)}
.f-col{position:absolute;top:4112px;color:var(--white);font-size:13px}
.f-col h4{font-size:20px;font-weight:600;margin-bottom:26px;font-family:var(--serif)}
.f-col li{list-style:none;line-height:25px;font-size:12.5px;position:relative;padding-left:20px}
.f-col li:before{content:"";position:absolute;left:2px;top:9px;border-left:6px solid var(--white);border-top:4px solid transparent;border-bottom:4px solid transparent}
.contact li{padding-left:26px}
.contact li:before{display:none}
.contact svg{position:absolute;left:0;top:7px}
.email-field{width:266px;height:40px;background:var(--white);font-size:12px;color:var(--muted);padding:12px}
.subscribe{margin-top:16px;width:134px;height:40px;line-height:40px;background:var(--brand);color:var(--white);text-align:center;font-size:13px;font-weight:700}
.copyright{position:absolute;left:100px;top:4344px;font-size:11.5px;color:var(--white)}
.social{position:absolute;top:4336px;width:28px;height:28px;border-radius:50%;background:var(--brand-soft)}
</style>
</head>
<body>

<header class="site-header">
  <div class="brand">#kindhearth</div>
  <nav class="nav">
    <a class="active" style="left:4px">Home</a>
    <a style="left:79px">About</a>
    <a style="left:150px">Events</a>
    <a style="left:227px">Blog</a>
    <a style="left:288px">Give</a>
    <a style="left:348px">Contact Us</a>
    <span class="social-sq abs" style="left:464px"></span>
  </nav>
</header>

<section class="hero">
  <div class="hero-photo" role="img" aria-label="Volunteers planting a young tree together in a grassy park"></div>
  <h1 class="hero-title">#kindhearth</h1>
  <a class="btn">Learn More</a>
  <svg class="hero-wave" width="1200" height="130" viewBox="0 0 1200 130">
    <polygon points="0,130 0,70 200,110 420,80 600,118 800,72 1000,105 1200,60 1200,130" fill="#fff"/>
    <polyline points="0,70 200,110 420,80 600,118 800,72 1000,105 1200,60" fill="none" stroke="#4c7991" stroke-width="7"/>
  </svg>
</section>

<section class="actions">
  <div class="action" style="left:98px">
    <svg width="48" height="44" viewBox="0 0 48 44" fill="none" stroke="#4c7991" stroke-width="2.5" stroke-linejoin="round"><path d="M24 22c-8-6-12-10-10-15 2-4 7-4 10 0 3-4 8-4 10 0 2 5-2 9-10 15z"/><path d="M4 20l8 14h24l8-14"/></svg>
    <h3>Donate Now</h3>
    <p>Lorem ipsum dolor sit amet, conset sadi elitr, sed diam nonumy eirmod tempor invidunt ut labore et dolore.</p>
    <a class="tag">View Details</a>
  </div>
  <div class="action featured" style="left:443px">
    <svg width="48" height="44" viewBox="0 0 48 44" fill="none" stroke="#fff" stroke-width="2.5"><circle cx="24" cy="22" r="16"/><circle cx="24" cy="22" r="6"/><path d="M24 6v10M24 28v10M8 22h10M30 22h10"/></svg>
    <h3>Volunteer Now</h3>
    <p>Lorem ipsum dolor sit amet, conset sadi elitr, sed diam nonumy eirmod tempor invidunt ut labore et dolore.</p>
    <a class="tag">View Details</a>
  </div>
  <div class="action" style="left:783px">
    <svg width="48" height="44" viewBox="0 0 48 44" fill="none" stroke="#4c7991" stroke-width="2.5" stroke-linejoin="round"><path d="M6 30l14-14 8 8 14-14"/><path d="M32 10h10v10"/><path d="M6 38h36"/></svg>
    <h3>Take Part Now</h3>
    <p>Lorem ipsum dolor sit amet, conset sadi elitr, sed diam nonumy eirmod tempor invidunt ut labore et dolore.</p>
    <a class="tag">View Details</a>
  </div>
</section>

<section class="band" style="top:1117px;height:600px">
  <svg class="abs" style="left:0;top:0" width="1200" height="40" viewBox="0 0 1200 40"><polygon points="0,0 1200,0 1200,8 900,22 600,6 300,24 0,10" fill="#fff"/></svg>
  <h2 class="band-title" style="top:52px">Project Events</h2>
  <svg class="abs" style="left:0;bottom:0" width="1200" height="70" viewBox="0 0 1200 70"><polygon points="0,70 0,40 180,60 360,34 560,66 760,30 980,58 1200,26 1200,70" fill="#fff"/></svg>
</section>
<div class="date" style="left:100px;top:1253px"><b>13</b><span>JUL</span></div>
<article class="event" style="left:163px;top:1250px">
  <div class="event-photo" role="img" aria-label="Group of volunteers smiling at a service project"></div>
  <h4>Nullam ac vestibulum orci, in mattis ipsum.</h4>
  <p>Lorem ipsum dolor sit amet, consectetur adipiscing elit. Morbi egestas arcu vel quam consequat</p>
  <a class="more">Read More...</a>
</article>
<div class="date" style="left:442px;top:1253px"><b>17</b><span>JUL</span></div>
<article class="event" style="left:505px;top:1250px">
  <div class="event-photo" role="img" aria-label="Volunteers working together outdoors"></div>
  <h4>Nullam ac vestibulum orci, in mattis ipsum.</h4>
  <p>Lorem ipsum dolor sit amet, consectetur adipiscing elit. Morbi egestas arcu vel quam consequat</p>
  <a class="more">Read More...</a>
</article>
<div class="date" style="left:785px;top:1253px"><b>21</b><span>JUL</span></div>
<article class="event" style="left:848px;top:1250px">
  <div class="event-photo" role="img" aria-label="Team cleaning up a park area"></div>
  <h4>Nullam ac vestibulum orci, in mattis ipsum.</h4>
  <p>Lorem ipsum dolor sit amet, consectetur adipiscing elit. Morbi egestas arcu vel quam consequat</p>
  <a class="more">Read More...</a>
</article>

<section class="story">
  <h2 class="story-title">Our Story</h2>
  <div class="story-sub">Working Toward a Better Tomorrow</div>
  <p class="story-text">What if we were known not by what we're against, but by what we're for? If our collective energy was invested in things that unite rather than divide, wouldn't we see stronger neighborhoods, healthier communities, and more resilient relationships? We believe so.</p>
  <a class="btn" style="left:92px;width:124px">Read More</a>
  <a class="btn" style="left:222px;width:124px">Contact</a>
  <svg class="story-frame" viewBox="0 0 466 352">
    <polygon points="220,0 466,0 466,352 120,352 120,330 444,330 444,20 220,20" fill="#4c7991"/>
  </svg>
  <div class="abs" role="img" aria-label="Smiling volunteer gardening in a community garden" style="left:644px;top:1827px;width:434px;height:312px;background:linear-gradient(135deg,#a7b3a8,#71876a 55%,#55694f);border:6px solid #fff;box-shadow:0 0 0 1px #ddd"></div>
</section>

<section class="band" style="top:2238px;height:705px">
  <div class="abs" role="img" aria-label="Soft blue-tinted photo of a smiling woman outdoors" style="left:0;top:0;width:1200px;height:705px;background:radial-gradient(circle at 25% 20%,rgba(140,180,200,.5),transparent 45%)"></div>
  <svg class="abs" style="left:0;top:0" width="1200" height="40" viewBox="0 0 1200 40"><polygon points="0,0 1200,0 1200,10 850,24 500,8 200,22 0,6" fill="#fff"/></svg>
  <h2 class="band-title" style="top:106px">Social Events</h2>
  <svg class="abs" style="left:0;bottom:0" width="1200" height="80" viewBox="0 0 1200 80"><polygon points="0,80 0,44 200,66 420,36 600,10 780,40 1000,62 1200,30 1200,80" fill="#fff"/></svg>
</section>
<div class="date" style="left:100px;top:2442px"><b>30</b><span>JUL</span></div>
<article class="event" style="left:163px;top:2439px">
  <div class="event-photo" role="img" aria-label="Friends gathered around a picnic table"></div>
  <h4>Nullam ac vestibulum orci, in mattis ipsum.</h4>
  <p>Lorem ipsum dolor sit amet, consectetur adipiscing elit. Morbi egestas arcu vel quam consequat</p>
  <a class="more">Read More...</a>
</article>
<div class="date" style="left:442px;top:2442px"><b>30</b><span>JUL</span></div>
<article class="event" style="left:505px;top:2439px">
  <div class="event-photo" role="img" aria-label="Group cheering with raised arms in a field"></div>
  <h4>Nullam ac vestibulum orci, in mattis ipsum.</h4>
  <p>Lorem ipsum dolor sit amet, consectetur adipiscing elit. Morbi egestas arcu vel quam consequat</p>
  <a class="more">Read More...</a>
</article>
<div class="date" style="left:785px;top:2442px"><b>30</b><span>JUL</span></div>
<article class="event" style="left:848px;top:2439px">
  <div class="event-photo" role="img" aria-label="Neighbors chatting together indoors"></div>
  <h4>Nullam ac vestibulum orci, in mattis ipsum.</h4>
  <p>Lorem ipsum dolor sit amet, consectetur adipiscing elit. Morbi egestas arcu vel quam consequat</p>
  <a class="more">Read More...</a>
</article>

<section class="testimonials">
  <h2 class="section-title" style="top:2976px">Testimonials</h2>
  <div class="avatar" role="img" aria-label="Portrait of a community member" style="left:104px;top:3098px;width:76px;height:76px"></div>
  <div class="avatar" role="img" aria-label="Portrait of a community member" style="left:233px;top:3098px;width:80px;height:80px"></div>
  <div class="avatar" role="img" aria-label="Portrait of a community member" style="left:366px;top:3094px;width:88px;height:88px"></div>
  <div class="avatar" role="img" aria-label="Portrait of the featured author" style="left:510px;top:3060px;width:176px;height:176px;border:2px solid #4c7991;box-shadow:0 0 0 6px #fff,0 4px 14px rgba(0,0,0,.15)"></div>
  <div class="avatar" role="img" aria-label="Portrait of a community member" style="left:740px;top:3094px;width:88px;height:88px"></div>
  <div class="avatar" role="img" aria-label="Portrait of a community member" style="left:882px;top:3098px;width:80px;height:80px"></div>
  <div class="avatar" role="img" aria-label="Portrait of a community member" style="left:1018px;top:3098px;width:76px;height:76px"></div>
  <div class="author">- BY AUTHOR NAME</div>
  <div class="author-loc">- City Location</div>
  <p class="quote">« Sed ut perspiciatis unde omnis iste natus error sit voluptatem accusantium doloremque laudantium, totam rem aperiam, eaque ipsa quae ab illo inventore veritatis et quasi architecto beatae vitae dicta sunt explicabo. »</p>
</section>

<section class="blog">
  <h2 class="section-title" style="top:3478px">Latest Blog</h2>
  <article class="post" style="top:3570px;height:150px">
    <div class="date"><b>03</b><span>JUL</span></div>
    <h4>What Is It Like To Help With a Home Build Project?</h4>
    <div class="meta">&#9679; By Someone<i>&#9632; 0</i></div>
    <div class="excerpt">Nor again is there anyone who loves or pursues or desires to obtain pain of itself, because it is pain but because occasionally circumstances</div>
  </article>
  <article class="post" style="top:3742px;height:64px">
    <div class="date"><b>03</b><span>JUL</span></div>
    <h4>10 Ways You Can Get Involved In Your Community!</h4>
    <div class="meta">&#9679; By Someone<i>&#9632; 0</i></div>
  </article>
  <article class="post" style="top:3818px;height:64px">
    <div class="date"><b>03</b><span>JUL</span></div>
    <h4>Working as a team</h4>
    <div class="meta">&#9679; By Someone<i>&#9632; 0</i></div>
  </article>
  <article class="feature" role="img" aria-label="Volunteers in matching shirts planting in a park">
    <div class="date"><b>03</b><span>JUL</span></div>
    <div class="tools">
      <svg width="92" height="56" viewBox="0 0 92 56" stroke="#fff" stroke-width="3" fill="none"><path d="M30 18v20M20 28h20"/><path d="M56 32l12-12M58 22a5 5 0 0 1 8 0M66 34a5 5 0 0 1-8 0"/></svg>
    </div>
    <p>Sed ut perspiciatis unde omnis iste natus error sit voluptatem accusantium doloremque laudantium, totam rem aperiam.</p>
  </article>
</section>

<footer class="footer">
  <svg class="abs" style="left:0;top:0" width="1200" height="90" viewBox="0 0 1200 90">
    <polygon points="0,90 0,48 180,66 380,30 560,52 720,6 900,44 1060,22 1200,50 1200,90" fill="#1b1b1b"/>
    <polyline points="0,48 180,66 380,30 560,52 720,6 900,44 1060,22 1200,50" fill="none" stroke="#4c7991" stroke-width="6"/>
  </svg>
  <div class="footer-base"></div>
</footer>
<div class="f-col contact" style="left:100px">
  <h4>CONTACT US</h4>
  <ul>
    <li><svg width="12" height="12" viewBox="0 0 12 12"><path d="M1 5l10-4-4 10-1-5z" fill="#fff"/></svg>2140 Maple Row, Hillcrest Lane,<br>Town Center</li>
    <li><svg width="12" height="12" viewBox="0 0 12 12"><path d="M2 1h3l1 3-2 1a7 7 0 0 0 3 3l1-2 3 1v3c-5 0-9-4-9-9z" fill="#fff"/></svg>800-555-0142</li>
    <li><svg width="12" height="12" viewBox="0 0 12 12"><rect x="0.5" y="2" width="11" height="8" fill="#fff"/><path d="M1 3l5 4 5-4" stroke="#1b1b1b" fill="none"/></svg>info@kindhearth.com</li>
  </ul>
</div>
<div class="f-col" style="left:358px">
  <h4>QUICK LINKS</h4>
  <ul><li>Home</li><li>About</li><li>Events</li><li>Blog</li><li>Give</li><li>Contact Us</li></ul>
</div>
<div class="f-col" style="left:588px">
  <h4>OTHER LINKS</h4>
  <ul><li>Company</li><li>Privacy Policy</li><li>Terms &amp; Conditions</li><li>Our Clients</li></ul>
</div>
<div class="f-col" style="left:840px">
  <h4>NEWSLETTER</h4>
  <div class="email-field">Email ID</div>
  <div class="subscribe">SUBSCRIBE</div>
</div>
<div class="copyright">Copyright © 2018. Allrights Reserved.</div>
<span class="social" style="left:990px"></span>
<span class="social" style="left:1028px"></span>
<span class="social" style="left:1066px"></span>
</body>
</html>
```